Zielgruppe
Steuerberater, Zielgruppe: Mandanten
Aufgabenstellung
Es sollten keine Balken an den Rändern vorhanden sein, so dass das Briefpapier mit dem eigenen Farbdrucker bedruckt werden kann.
-Keine Balken an den Rändern
-Wir wollen kein Briefpapier bedrucken lassen, soll mit dem eigenen Drucker bedruckbar sein
Die Schriftart CG Omega sollte installiert sein, für die korrekte Darstellung.

```html
<!DOCTYPE html>
<html lang="de">
<head>
<meta charset="utf-8">
<title>Briefbogen Kanzlei Velmar</title>
<link rel="stylesheet" href="https://fonts.googleapis.com/css2?family=Arimo:wght@400;700&display=swap">
<style>
  :root {
    --backdrop: #eceef2;
    --paper: #ffffff;
    --brand: #2b3a78;
    --ink: #111111;
    --muted: #555555;
    --rule: #bbbbbb;
    --signature: #e6e6e8;
  }
  * { margin: 0; padding: 0; box-sizing: border-box; }
  html, body { width: 928px; height: 1200px; overflow: hidden; }
  body { background: var(--backdrop); font-family: "Arimo", Arial, sans-serif; color: var(--ink); }
  .sheet { position: absolute; left: 40px; top: 0; width: 848px; height: 1200px; background: var(--paper); }
  .brand { position: absolute; left: 520px; top: 70px; display: flex; align-items: center; gap: 14px; }
  .brand-dot { width: 26px; height: 26px; border-radius: 50%; background: var(--brand); }
  .brand-text { color: var(--brand); }
  .brand-name { font-size: 34px; font-weight: 400; line-height: 1.1; display: block; }
  .brand-tagline { font-size: 11px; letter-spacing: 2.4px; display: block; margin-top: 6px; }
  .sender-line { position: absolute; left: 108px; top: 168px; font-size: 9px; color: var(--muted); }
  .sender-line strong { color: var(--brand); }
  .recipient { position: absolute; left: 108px; top: 212px; font-size: 16.5px; line-height: 21px; }
  .contact { position: absolute; left: 630px; top: 217px; font-size: 11.5px; line-height: 16px; color: #333; }
  .contact .person { color: var(--brand); font-weight: 700; }
  .contact .block { margin-bottom: 6px; }
  .contact .icon-row { display: flex; align-items: center; gap: 4px; }
  .contact svg { width: 11px; height: 11px; fill: var(--brand); }
  .fold-mark { position: absolute; left: 9px; width: 11px; height: 1px; background: var(--rule); }
  .fold-mark.upper { top: 406px; }
  .fold-mark.lower { top: 774px; }
  .letter { position: absolute; left: 108px; top: 408px; width: 684px; font-size: 16.5px; line-height: 22.8px; }
  .subject { margin-bottom: 46px; }
  .salutation { margin-bottom: 23px; }
  .letter p.body { text-align: justify; margin-bottom: 23px; }
  .signature { position: absolute; left: 108px; top: 980px; width: 260px; height: 52px; background: var(--signature); border-radius: 4px; }
</style>
</head>
<body>
<main class="sheet">
  <header class="brand">
    <span class="brand-dot"></span>
    <span class="brand-text">
      <span class="brand-name">Kanzlei Velmar</span>
      <span class="brand-tagline">STEUERBERATER | RECHTSANWALT</span>
    </span>
  </header>

  <div class="sender-line"><strong>Kanzlei Velmar</strong> · Kastanienweg 14 · 70999 Birkenfeld</div>

  <address class="recipient" style="font-style:normal">
    Musterfirma<br>z. Hd. Herrn Mustermann<br>Musterstraße 1<br>01234 Musterstadt
  </address>

  <aside class="contact">
    <div class="block"><span class="person">Tarek Velmar</span><br>Diplom-Kaufmann<br>Steuerberater</div>
    <div class="block"><span class="person">Aron Velmar</span><br>Rechtsanwalt<br>Fachanwalt für Steuerrecht</div>
    <div class="block">Kastanienweg 14<br>70999 Birkenfeld</div>
    <div class="block">
      <div class="icon-row"><svg viewBox="0 0 24 24"><path d="M6.6 10.8a15 15 0 0 0 6.6 6.6l2.2-2.2a1 1 0 0 1 1-.25 11.4 11.4 0 0 0 3.6.57 1 1 0 0 1 1 1V20a1 1 0 0 1-1 1A17 17 0 0 1 3 4a1 1 0 0 1 1-1h3.5a1 1 0 0 1 1 1c0 1.25.2 2.45.57 3.57a1 1 0 0 1-.25 1z"/></svg>07000 412003</div>
      <div class="icon-row"><svg viewBox="0 0 24 24"><path d="M6 2h12v6H6zM4 9h16a2 2 0 0 1 2 2v7h-4v4H6v-4H2v-7a2 2 0 0 1 2-2zm4 8v3h8v-3z"/></svg>07000 412005</div>
    </div>
    <div>
      <div class="icon-row"><svg viewBox="0 0 24 24"><path d="M2 5h20v14H2zm2 2v.5l8 5 8-5V7z"/></svg>mail@kanzlei-velmar.de</div>
      <div class="icon-row"><svg viewBox="0 0 24 24"><circle cx="12" cy="12" r="10"/></svg>www.kanzlei-velmar.de</div>
    </div>
  </aside>

  <span class="fold-mark upper"></span>
  <span class="fold-mark lower"></span>

  <article class="letter">
    <p class="subject">Betreff</p>
    <p class="salutation">Sehr geehrte Damen und Herren,</p>
    <p class="body">Lorem ipsum dolor sit amet, consectetuer adipiscing elit, sed diam nonummy nibh euismod tincidunt ut laoreet dolore magna aliquam erat volutpat. Ut wisi enim ad minim veniam, quis nostrud exerci tation ullamcorper suscipit lobortis nisl ut aliquip ex ea commodo consequat. Duis autem vel eum iriure dolor in hendrerit in vulputate velit esse molestie consequat, vel illum dolore eu feugiat nulla facilisis at vero eros et accumsan et iusto odio dignissim qui blandit praesent luptatum zzril delenit augue duis dolore te feugait nulla facilisi.<br>Lorem ipsum dolor sit amet, cons ectetuer adipiscing elit, sed diam nonummy</p>
    <p class="body">Lorem ipsum dolor sit amet, consectetuer adipiscing elit, sed diam nonummy nibh euismod tincidunt ut laoreet dolore magna aliquam erat volutpat. Ut wisi enim ad minim veniam, quis nostrud exerci tation ullamcorper suscipit lobortis nisl ut aliquip ex ea commodo consequat. Duis autem vel eum iriure dolor in hendrerit in vulputate velit esse molestie consequat, vel illum dolore eu feugiat nulla facilisis at vero eros et accumsan et iusto odio dignissim qui blandit praesent luptatum zzril delenit augue duis dolore te feugait nulla facilisi.<br>Lorem ipsum dolor sit amet, cons ectetuer adipiscing elit, sed diam nonummy</p>
    <p>Mit freundlichen Grüßen</p>
  </article>

  <div class="signature" role="img" aria-label="Handschriftliche Unterschrift Max Mustermann"></div>
</main>
</body>
</html>
```